Design an authentic and very luxury business card for a company

Design an authentic and very luxury standart size business card 90x50 mm

On the first side of the business card we need only logo of our company group with nice backround. Logo of company group is the first attached file called "gold". The name of coumpany group is "Verdant harbor group".

On the other side of business card should be given information which you will find in the second file and the logo of the company VHG AERO. Logo is attached too (third file)

We prefer having both sides of the business card in different colours to make them look more unique and the edge of business card can have its own colour too. Business card could also have patterns and/or indentations (like the last attached file as an example).The way how you design the information about partilucar contact person, websites and adresses - is completely up to you. We need authentic and luxury looking business card. If need you more information or you need logos in other formats I will provide everything gladly.

Last two files I attached only as an examples to show what looks quite well from our point of view. What concerns manufacturing of business cards - we are completely open so if you see that your proposed design will look exceptionally well with particular production type - we are open for your ideas.

If you need further information feel free to contact us.

Best regards

```html
<!DOCTYPE html>
<html lang="en">
<head>
<meta charset="utf-8">
<title>Verdant harbor group – business card</title>
<link href="https://fonts.googleapis.com/css2?family=Lato:wght@400;700&family=Montserrat:wght@600&display=swap" rel="stylesheet">
<style>
  :root {
    --page-bg: #3a3b3d;
    --card-front: #2b2b2d;
    --card-back: #2f3032;
    --band: #4a4b4e;
    --band-dark: #3c3d40;
    --gold: #e2ad2b;
    --blue: #2a8fd8;
    --text-light: #e6e6e6;
    --text-muted: #b9babc;
  }
  * { box-sizing: border-box; margin: 0; padding: 0; }
  html, body { width: 1200px; height: 900px; overflow: hidden; }
  body {
    background: var(--page-bg);
    display: flex;
    align-items: center;
    justify-content: center;
    gap: 40px;
    font-family: "Lato", sans-serif;
  }
  .card {
    position: relative;
    width: 520px;
    height: 289px;
    border-radius: 18px;
    overflow: hidden;
  }

  /* Front side */
  .card-front { background: var(--card-front); }
  .front-texture {
    position: absolute; inset: 0;
    background: linear-gradient(135deg, #2f2f31 0%, #262628 50%, #2f2f31 100%);
  }
  .group-brand {
    position: absolute;
    left: 0; right: 0; top: 92px;
    display: flex; flex-direction: column; align-items: center; gap: 14px;
    font-family: "Montserrat", sans-serif;
    font-weight: 600;
    color: var(--gold);
  }
  .brand-square { width: 44px; height: 44px; background: var(--gold); }
  .brand-name { font-size: 24px; letter-spacing: 1px; text-transform: uppercase; }

  /* Back side */
  .card-back { background: var(--card-back); }
  .aero-brand {
    position: absolute; right: 48px; top: 46px;
    font-family: "Lato", sans-serif;
    font-weight: 700; font-size: 34px;
    color: var(--blue);
    letter-spacing: 1px;
  }
  .contact-person { position: absolute; left: 0; top: 112px; }
  .person-marker {
    position: absolute; left: 0; top: 6px;
    width: 8px; height: 30px; background: var(--blue);
  }
  .person-name {
    padding-left: 22px;
    font-weight: 700; font-size: 21px; color: var(--blue);
  }
  .person-role {
    padding-left: 22px;
    font-size: 12px; color: var(--text-light);
  }
  .contact-list {
    position: absolute; left: 22px; top: 172px;
    list-style: none;
    font-size: 11px; color: var(--text-muted);
  }
  .contact-list li { display: flex; align-items: center; gap: 10px; height: 18px; }
  .contact-icon { width: 12px; height: 12px; fill: var(--text-muted); }

  .info-band {
    position: absolute; left: 0; right: 0; top: 208px; bottom: 0;
    background: var(--band);
    border-top: 1px solid var(--gold);
  }
  .web-marker {
    position: absolute; left: 0; top: 8px;
    width: 30px; height: 16px; background: var(--blue);
  }
  .web-list {
    position: absolute; left: 44px; top: 4px;
    font-size: 11px; color: var(--text-light); line-height: 13px;
  }
  .address-strip {
    position: absolute; left: 0; right: 0; top: 34px; bottom: 12px;
    background: var(--band-dark);
    border-top: 1px solid var(--gold);
    display: flex; align-items: center; gap: 12px;
    padding-left: 22px;
  }
  .address-strip .contact-icon { fill: var(--gold); }
  .address-text { font-size: 11px; color: var(--text-muted); line-height: 14px; }
</style>
</head>
<body>

  <section class="card card-front">
    <div class="front-texture" role="img" aria-label="Diagonal pinstripe texture in dark charcoal"></div>
    <div class="group-brand">
      <span class="brand-square"></span>
      <span class="brand-name">Verdant harbor group</span>
    </div>
  </section>

  <section class="card card-back">
    <div class="aero-brand">VHG AERO</div>

    <div class="contact-person">
      <span class="person-marker"></span>
      <p class="person-name">Lukas Varnelis</p>
      <p class="person-role">CEO/Vorstandsvorsitzender</p>
    </div>

    <ul class="contact-list">
      <li>
        <svg class="contact-icon" viewBox="0 0 24 24"><path d="M6.6 10.8a15 15 0 0 0 6.6 6.6l2.2-2.2c.3-.3.7-.4 1-.2 1.1.4 2.3.6 3.6.6.6 0 1 .4 1 1V20c0 .6-.4 1-1 1A17 17 0 0 1 3 4c0-.6.4-1 1-1h3.5c.6 0 1 .4 1 1 0 1.3.2 2.5.6 3.6.1.3 0 .7-.2 1z"/></svg>
        <span>+4915550142207</span>
      </li>
      <li>
        <svg class="contact-icon" viewBox="0 0 24 24"><path d="M2 5h20v14H2z M2 5l10 8 10-8" fill="none" stroke="#b9babc" stroke-width="2"/></svg>
        <span>lukas@vhgaero.com</span>
      </li>
    </ul>

    <div class="info-band">
      <span class="web-marker"></span>
      <div class="web-list">
        <p>www.vhg-group.com</p>
        <p>www.vhgaero.com</p>
      </div>
      <div class="address-strip">
        <svg class="contact-icon" viewBox="0 0 24 24"><path d="M12 2a7 7 0 0 0-7 7c0 5 7 13 7 13s7-8 7-13a7 7 0 0 0-7-7zm0 9.5A2.5 2.5 0 1 1 12 6.5a2.5 2.5 0 0 1 0 5z"/></svg>
        <div class="address-text">
          <p>Lindenweg 7, 80331 München, Bayern,</p>
          <p>Germany Saulės g. 14, 01100 Vilnius, Lithuania</p>
        </div>
      </div>
    </div>
  </section>

</body>
</html>
```